Business card por a urban DJ, up scale audience target

Need a sober design, modern, conservative colors but i can consider some options, y play rnb, hip hop, EDM and top40.

Business card for contact and personal info, double sided, use logo attrached please; im 42 so i need a card acording to my age an target audience.

Target Market(s)

Adult people, up scale audience

Industry/Entity Type

Music Download

Contact Information for Business Card

Cel (318) 5024471963 www.kelvarodun.com

Requirements
Must have
• open mind
Nice to have
• open mind
Should not have
• DJ

```html
<!DOCTYPE html>
<html lang="en">
<head>
<meta charset="utf-8">
<title>Kelva – Business Card</title>
<link href="https://fonts.googleapis.com/css2?family=Open+Sans:wght@400;700&display=swap" rel="stylesheet">
<style>
  :root {
    --bg: #2b2b2b;
    --card: #000000;
    --ink: #c4c4c4;
    --ink-soft: #a9a9a9;
  }
  html, body {
    margin: 0;
    width: 1200px;
    height: 900px;
    overflow: hidden;
    background: var(--bg);
    font-family: "Open Sans", sans-serif;
  }
  .card {
    position: absolute;
    width: 640px;
    height: 366px;
    background: var(--card);
    box-shadow: 0 14px 30px rgba(0,0,0,.45);
    overflow: hidden;
  }
  .card--front { left: 90px; top: 60px; }
  .card--back  { left: 470px; top: 474px; }

  .brand-name {
    position: absolute;
    margin: 0;
    color: var(--ink);
    font-weight: 700;
    line-height: 1;
    letter-spacing: 2px;
  }
  .card--front .brand-name { left: 52px; top: 140px; font-size: 90px; }
  .card--back .brand-name { left: 40px; top: 144px; font-size: 76px; }

  .front-url {
    position: absolute;
    left: 56px;
    top: 262px;
    color: var(--ink);
    font-size: 20px;
    letter-spacing: 4px;
  }
  .equalizer {
    position: absolute;
    fill: var(--ink);
  }
  .card--front .equalizer { right: 24px; bottom: 34px; width: 260px; height: 90px; }
  .card--back .equalizer  { right: 24px; bottom: 70px; width: 270px; height: 92px; }

  .holder {
    position: absolute;
    right: 44px;
    top: 26px;
    text-align: right;
    color: var(--ink);
  }
  .holder__name { font-size: 19px; font-weight: 700; }
  .holder__role { font-size: 9px; margin-top: -2px; }
  .edge-tab {
    position: absolute;
    right: 18px;
    top: 24px;
    width: 16px;
    height: 42px;
    background: var(--ink);
  }
  .rule {
    position: absolute;
    height: 2px;
    background: var(--ink-soft);
  }
  .rule--top { left: 24px; right: 24px; top: 116px; }
  .rule--bottom { left: 30px; right: 250px; bottom: 32px; }

  .contacts {
    position: absolute;
    left: 34px;
    bottom: 42px;
    margin: 0;
    padding: 0;
    list-style: none;
    color: var(--ink);
    font-size: 14px;
    line-height: 18px;
  }
  .contacts li { display: flex; align-items: center; gap: 7px; }
  .contacts svg { width: 10px; height: 12px; fill: none; stroke: var(--ink); stroke-width: 1.5; }
</style>
</head>
<body>

<section class="card card--front">
  <p class="brand-name">KELVA</p>
  <div class="front-url">www.kelvarodun.com</div>
  <svg class="equalizer" viewBox="0 0 300 96" preserveAspectRatio="none" aria-hidden="true">
    <rect x="0" y="80" width="8" height="16"/><rect x="12" y="72" width="8" height="24"/>
    <rect x="24" y="84" width="8" height="12"/><rect x="36" y="68" width="8" height="28"/>
    <rect x="48" y="80" width="8" height="16"/><rect x="60" y="74" width="8" height="22"/>
    <rect x="72" y="86" width="8" height="10"/><rect x="84" y="66" width="8" height="30"/>
    <rect x="96" y="60" width="8" height="36"/><rect x="108" y="74" width="8" height="22"/>
    <rect x="120" y="56" width="8" height="40"/><rect x="132" y="64" width="8" height="32"/>
    <rect x="144" y="50" width="8" height="46"/><rect x="156" y="62" width="8" height="34"/>
    <rect x="168" y="54" width="8" height="42"/><rect x="180" y="66" width="8" height="30"/>
    <rect x="192" y="48" width="8" height="48"/><rect x="204" y="40" width="8" height="56"/>
    <rect x="216" y="52" width="8" height="44"/><rect x="228" y="34" width="8" height="62"/>
    <rect x="240" y="44" width="8" height="52"/><rect x="252" y="28" width="8" height="68"/>
    <rect x="264" y="36" width="8" height="60"/><rect x="276" y="14" width="8" height="82"/>
    <rect x="288" y="4" width="8" height="92"/>
  </svg>
</section>

<section class="card card--back">
  <div class="holder">
    <div class="holder__name">Tomas Arevald</div>
    <div class="holder__role">CEO</div>
  </div>
  <div class="edge-tab"></div>
  <div class="rule rule--top"></div>
  <p class="brand-name">KELVA</p>
  <svg class="equalizer" viewBox="0 0 300 96" preserveAspectRatio="none" aria-hidden="true">
    <rect x="0" y="82" width="8" height="14"/><rect x="12" y="76" width="8" height="20"/>
    <rect x="24" y="86" width="8" height="10"/><rect x="36" y="70" width="8" height="26"/>
    <rect x="48" y="82" width="8" height="14"/><rect x="60" y="74" width="8" height="22"/>
    <rect x="72" y="86" width="8" height="10"/><rect x="84" y="66" width="8" height="30"/>
    <rect x="96" y="58" width="8" height="38"/><rect x="108" y="72" width="8" height="24"/>
    <rect x="120" y="56" width="8" height="40"/><rect x="132" y="64" width="8" height="32"/>
    <rect x="144" y="52" width="8" height="44"/><rect x="156" y="60" width="8" height="36"/>
    <rect x="168" y="54" width="8" height="42"/><rect x="180" y="66" width="8" height="30"/>
    <rect x="192" y="46" width="8" height="50"/><rect x="204" y="40" width="8" height="56"/>
    <rect x="216" y="50" width="8" height="46"/><rect x="228" y="32" width="8" height="64"/>
    <rect x="240" y="42" width="8" height="54"/><rect x="252" y="26" width="8" height="70"/>
    <rect x="264" y="36" width="8" height="60"/><rect x="276" y="14" width="8" height="82"/>
    <rect x="288" y="4" width="8" height="92"/>
  </svg>
  <ul class="contacts">
    <li><svg viewBox="0 0 10 12"><rect x="1.5" y="0.75" width="7" height="10.5" rx="1"/></svg>(318) 5024471963</li>
    <li><svg viewBox="0 0 10 12"><circle cx="5" cy="6" r="4.2"/><path d="M0.8 6h8.4M5 1.8c-2 2.5-2 5.9 0 8.4M5 1.8c2 2.5 2 5.9 0 8.4"/></svg>www.kelvarodun.com</li>
  </ul>
  <div class="rule rule--bottom"></div>
</section>

</body>
</html>
```